Classic and neutral book cover design

We are looking for a classic and neutral book cover design to be used as the template for a series of books to be published. We are hence looking for a template that will allow us to easily change the title name for all books in this series.
The use of very few colours (black and white is welcome) and few design elements is a big bonus. As a source of inspiration we would like to ask you to view the very simple and
If you think you have a cool idea that can add a twist to the formal classic look don't hesitate. Go for it !
Work will be done for a 30 year old Sweden based cultural non-profit called VĂ©ru (www.veruhaus-example.org). We work with the publishing and supporting of post-modern art and literature addressing contemporary topics but are also involved in assisting projects of cultural preservation.
Target Market(s)
The audience is expected to have some form of interest in culture but could range from hobbyist readers to tenure track scholars
Industry/Entity Type
Non-Profit
Requirements
Must have
- General:
- Classic and neutral feel
- Preferably very simple and few shapes
- usage of few colours (black and white is welcome)
Information to be displayed on the cover is:
- Author
- Title
- type of work e.g. play/novel (optional)
- publishing house (in this case "Veru Publishing")
Nice to have
- ideas to prevent it from become boring are of course welcome
Should not have
- - too many colours

```html
<!DOCTYPE html>
<html lang="en">
<head>
<meta charset="utf-8">
<title>Nice Title, Veru Publishing</title>
<link rel="stylesheet" href="https://fonts.googleapis.com/css2?family=Crimson+Text:ital,wght@0,400;1,400&display=swap">
<style>
  :root {
    --paper: #ffffff;
    --ink: #111111;
  }
  html, body {
    margin: 0;
    padding: 0;
    width: 952px;
    height: 1200px;
    overflow: hidden;
    background: var(--paper);
  }
  .cover {
    position: relative;
    width: 952px;
    height: 1200px;
    background: var(--paper);
    color: var(--ink);
    font-family: "Crimson Text", Georgia, serif;
  }
  .cover-frame {
    position: absolute;
    inset: 0;
  }
  .cover-line {
    position: absolute;
    left: 0;
    width: 100%;
    text-align: center;
    line-height: 1;
    margin: 0;
  }
  .publisher {
    top: 183px;
    font-size: 17px;
    font-style: italic;
    letter-spacing: 0.2em;
    text-indent: 0.2em;
    text-transform: uppercase;
  }
  .title {
    top: 420px;
    font-size: 92px;
    font-weight: 400;
    letter-spacing: 0.2em;
    text-indent: 0.2em;
  }
  .work-type {
    top: 792px;
    font-size: 28px;
    font-style: italic;
  }
  .byline {
    top: 845px;
    font-size: 18px;
    font-style: italic;
  }
  .author {
    top: 880px;
    font-size: 29px;
    letter-spacing: 0.14em;
    text-indent: 0.14em;
  }
</style>
</head>
<body>
  <main class="cover">
    <svg class="cover-frame" width="952" height="1200" viewBox="0 0 952 1200" aria-hidden="true">
      <rect x="43" y="43" width="866" height="1122" fill="none" stroke="var(--ink)" stroke-width="2.5"/>
      <rect x="58" y="58" width="836" height="1092" fill="none" stroke="var(--ink)" stroke-width="2.5"/>
    </svg>
    <p class="cover-line publisher">Veru Publishing</p>
    <h1 class="cover-line title">NICE TITLE</h1>
    <p class="cover-line work-type">Novel</p>
    <p class="cover-line byline">by</p>
    <p class="cover-line author">Author Authorson</p>
  </main>
</body>
</html>
```